Design a menu for health restaurant

A health food restaurant in Los Angeles is seeking menu design. Our foods are made from scratch using whole ingredients.
Name: Grubb Larder
Address: 1000 E 60th StLos Angeles, CA 90247
Website: www.GrubbLarder.example
We are looking for a clean and simple menu. Brand colors are white/tan, green and orange.

Please see attached excel with menu items and logo. We do not yet have prices.

Colors
f78f20
9bcb3c
ffffff
fff3d1

Requirements
Must have
• Easy to read.
Trifold menu design (front and back).
VEGAN, VEGETARIAN, GLUTEN FREE, CONTAINS NUTS symbols.
Logo.
Nice to have
• Incorporate brand colors, but still be easy to read.
We would like to use the Belco font (attached) if it works. If not we are open to a similar font that is easy to read.

Please see attached images.
We like the images and headers of OPTION 1. Would like something similar in trifold format.
We like the clean fonts of OPTION 2.

```html
<!DOCTYPE html>
<html lang="en">
<head>
<meta charset="utf-8">
<title>Grubb Larder — Menu</title>
<link rel="stylesheet" href="https://fonts.googleapis.com/css2?family=Titan+One&family=Baloo+2:wght@800&family=Didact+Gothic&display=swap">
<style>
  :root {
    --orange: #f78f20;
    --green: #9bcb3c;
    --green-fill: #aed36a;
    --cream: #fff3d1;
    --white: #ffffff;
    --pink: #f9cdb9;
    --ink: #111111;
  }
  * { box-sizing: border-box; margin: 0; padding: 0; }
  html, body { width: 1200px; height: 929px; overflow: hidden; background: var(--white); }
  .menu { position: relative; width: 1200px; height: 929px; font-family: "Didact Gothic", sans-serif; color: var(--ink); }
  .frame { position: absolute; overflow: visible; }
  .fill { position: absolute; border-radius: 14px; }
  .fill.wraps { left: 38px; top: 600px; width: 340px; height: 272px; background: var(--pink); }
  .fill.combos { left: 845px; top: 690px; width: 345px; height: 180px; background: var(--green-fill); }
  .section-title {
    position: absolute; font-family: "Titan One", sans-serif; font-style: italic;
    font-size: 21px; line-height: 1; color: var(--ink); background: var(--cream);
    border: 3px solid var(--orange); border-radius: 16px; padding: 2px 9px 3px 8px; letter-spacing: .5px;
  }
  .section-body { position: absolute; font-size: 15.2px; line-height: 18.2px; white-space: nowrap; }
  .item { margin-bottom: 4.5px; }
  .item-name { font-family: "Baloo 2", sans-serif; font-weight: 800; font-size: 14.2px; line-height: 18.2px; display: flex; align-items: center; gap: 6px; }
  .item-name .sub { display: block; font-size: 10.5px; line-height: 11px; }
  .tag { width: 14px; height: 14px; display: inline-block; }
  .tag-note { font-family: "Didact Gothic", sans-serif; font-weight: 400; font-size: 9px; margin-left: -3px; }
  .legend { position: absolute; left: 448px; top: 860px; display: flex; gap: 20px; font-size: 11.5px; align-items: center; }
  .legend span { display: flex; align-items: center; gap: 3px; }
  .legend .tag { width: 17px; height: 17px; }
</style>
</head>
<body>
<svg width="0" height="0" style="position:absolute">
  <defs>
    <symbol id="icon-vegan" viewBox="0 0 20 20"><rect x="1.5" y="1.5" width="17" height="17" fill="none" stroke="#111" stroke-width="1.3"/><text x="10" y="14.5" font-size="10" text-anchor="middle" font-family="sans-serif">V+</text></symbol>
    <symbol id="icon-vegetarian" viewBox="0 0 20 20"><path d="M1.5 1.5 L10 4 L18.5 1.5 L16 10 L18.5 18.5 L10 16 L1.5 18.5 L4 10 Z" fill="none" stroke="#111" stroke-width="1.2"/><text x="10" y="14" font-size="10" text-anchor="middle" font-family="sans-serif">V</text></symbol>
    <symbol id="icon-nuts" viewBox="0 0 20 20"><path d="M5 2 L15 2 L19 10 L15 18 L5 18 L1 10 Z" fill="none" stroke="#111" stroke-width="1.2"/><text x="10" y="13.5" font-size="8.5" text-anchor="middle" font-family="sans-serif">N+</text></symbol>
    <symbol id="icon-gf" viewBox="0 0 20 20"><circle cx="10" cy="10" r="8.5" fill="none" stroke="#111" stroke-width="1.3"/><text x="10" y="13.5" font-size="9" text-anchor="middle" font-family="sans-serif">GF</text></symbol>
  </defs>
</svg>

<main class="menu">
  <!-- dotted frames -->
  <svg class="frame" style="left:0;top:0" width="1200" height="929">
    <g fill="none" stroke="var(--orange)" stroke-width="8" stroke-linecap="round" stroke-dasharray="0 23">
      <rect x="32" y="64" width="358" height="490" rx="26"/>
      <rect x="457" y="62" width="342" height="497" rx="24"/>
      <rect x="842" y="62" width="334" height="582" rx="24"/>
    </g>
    <rect x="434" y="840" width="393" height="57" rx="16" fill="none" stroke="#111" stroke-width="5" stroke-linecap="round" stroke-dasharray="0 13"/>
  </svg>
  <div class="fill wraps"></div>
  <div class="fill combos"></div>

  <h2 class="section-title" style="left:46px;top:50px">Breakfast</h2>
  <h2 class="section-title" style="left:470px;top:50px">Burgers N’ Sammies</h2>
  <h2 class="section-title" style="left:846px;top:50px">Bowls</h2>
  <h2 class="section-title" style="left:44px;top:587px">Wraps</h2>
  <h2 class="section-title" style="left:472px;top:588px">Soups</h2>
  <h2 class="section-title" style="left:848px;top:677px">Combos</h2>

  <section class="section-body" style="left:54px;top:76px">
    <div class="item"><div class="item-name">Pastries <svg class="tag"><use href="#icon-vegetarian"/></svg></div>Croissant (regular, almond, chocolate)<br>Blueberry Muffin<br>Superseed Cookie</div>
    <div class="item"><div class="item-name">Parfait <svg class="tag"><use href="#icon-vegetarian"/></svg></div>Fresh strawberries and blueberries on yogurt<br>and muesli and topped with honey drizzle.</div>
    <div class="item"><div class="item-name">Avocado Super Toast <svg class="tag"><use href="#icon-vegan"/></svg></div>Avocado Mash, Tomato, Basil, Ground Flax,<br>Hemp Seed, Chickpeas, and Moringa Powder<br>on Whole Wheat Bread.</div>
    <div class="item"><div class="item-name">Brunch Burger</div>House seasoned beef burger topped with an<br>over medium egg, red leaf lettuce, tomato,<br>housemade pickles and Larder Sauce on a<br>bun.</div>
    <div class="item"><div class="item-name">Breakfast Sammy <svg class="tag" style="margin-left:22px"><use href="#icon-vegan"/></svg><span class="tag-note">option</span></div>Your choice of over medium egg or tofu steak<br>with guacamole, tomato, and Larder sauce<br>on an English muffin.</div>
    <div class="item"><div class="item-name">AM Burrito <svg class="tag" style="margin-left:24px"><use href="#icon-vegetarian"/></svg></div>Scrambled eggs, onion, red bell pepper, black<br>beans, housemade salsa, yogurt, and pepper<br>jack cheese in a tortilla.</div>
  </section>

  <section class="section-body" style="left:480px;top:76px">
    <div class="item"><div class="item-name">Air Fried Chicken Sammy</div>Air fried chicken breast topped with red leaf<br>lettuce, tomato, house made pickles and<br>Larder Sauce on a bun served with choice<br>of salad of fries.</div>
    <div class="item"><div class="item-name">Grilled Chicken Sammy</div>Grilled chicken topped with guacamole, red<br>leaf lettuce, tomato, house made pickles and<br>Larder Sauce. Served with regular fries or<br>side salad.</div>
    <div class="item"><div class="item-name">Classic Beef Burger</div>House seasoned beef burger topped with red<br>leaf lettuce, tomato, cheddar cheese, house<br>made pickles and Larder Sauce on a bun<br>served with choice of salad of fries.</div>
    <div class="item"><div class="item-name">Black Bean Pine Nut Burger <svg class="tag" style="margin-left:30px"><use href="#icon-vegan"/></svg><svg class="tag"><use href="#icon-nuts"/></svg></div>House made black bean pine nut burger<br>topped with red leaf lettuce, tomato, house<br>made pickles and mustard aioli on a bun<br>served with choice of salad of fries.</div>
    <div class="item"><div class="item-name">Salmon Burger</div>House made salmon burger topped with red<br>leaf lettuce, tomato, house made pickles and<br>Larder yogurt on a bun served with choice<br>of salad of fries.</div>
  </section>

  <section class="section-body" style="left:855px;top:76px">
    <div class="item"><div class="item-name">Southwest Bowl <svg class="tag" style="margin-left:6px"><use href="#icon-gf"/></svg><svg class="tag"><use href="#icon-nuts"/></svg></div>Your choice of protein with corn, black beans,<br>red onions, almonds and avocado over<br>quinoa with lime hot sauce.</div>
    <div class="item"><div class="item-name">Chimi Bowl <svg class="tag" style="margin-left:34px"><use href="#icon-gf"/></svg></div>Your choice of protein with red bell pepper,<br>mushrooms, zucchini, squash, onion, cherry<br>tomatoes and fresh herb chimichurri on wild<br>and brown rice.</div>
    <div class="item"><div class="item-name">Soba Noodle Bowl</div>Your choice of protein with spinach, snow<br>peas, roasted carrots, red bell pepper, cilantro,<br>sesame seeds and ginger lime sauce over<br>soba noodles.</div>
    <div class="item"><div class="item-name">Hollywood Bowl <svg class="tag" style="margin-left:16px"><use href="#icon-gf"/></svg></div>Your choice of protein with broccoli, roasted<br>corn, cherry tomatoes, basil, pepitas, flax seeds<br>and lemon juice on wild and brown rice.</div>
    <div class="item"><div class="item-name">Larder Bowl</div>Your choice of protein with roasted chickpeas<br>and cauliflower, zesty fennel salad and<br>citrus yogurt.</div>
    <div class="item"><div class="item-name">Buddha Bowl</div>Your choice of protein with corn, red kale,<br>sweet potatoes, red cabbage, parsley, oregano,<br>hummus, and farro.</div>
    <div class="item"><div class="item-name">Chili Rice Bowl</div>Chicken, onions, bell peppers, jalapeños, black<br>&amp; kidney beans, and tomato over brown rice.</div>
  </section>

  <section class="section-body" style="left:54px;top:613px">
    <div class="item"><div class="item-name">Rancher’s Wrap</div>Tomato, red onion, hard boiled egg, avocado,<br>feta cheese, microgreens, romaine, grilled<br>chicken and Ranch dressing in a grilled wrap.</div>
    <div class="item"><div class="item-name">Vegan Tuna Wrap <svg class="tag" style="margin-left:10px"><use href="#icon-vegan"/></svg></div>Vegan tuna, romaine, avocado, celery, shallot,<br>and oregano with Herbalicious Sauce in a<br>whole grain wrap.</div>
    <div class="item"><div class="item-name">Vegetarian Wrap <svg class="tag" style="margin-left:14px"><use href="#icon-vegetarian"/></svg></div>Roasted chickpeas, romaine, avocado, red bell<br>pepper, shaved carrots, cucumber, spinach,<br>basil, black beans and feta with lemon-<br>hummus in a sprouted 7-grain wrap.</div>
  </section>

  <section class="section-body" style="left:480px;top:614px">
    <div class="item"><div class="item-name">Chicken Noodle <svg class="tag" style="margin-left:40px"><use href="#icon-gf"/></svg></div>Chicken, egg noodles, root vegetables,<br>oregano &amp; peppercorns.</div>
    <div class="item"><div class="item-name">Larder Chili <svg class="tag" style="margin-left:66px"><use href="#icon-gf"/></svg></div>Chicken, onions, bell peppers, jalapeños, black<br>&amp; kidney beans, and tomato.</div>
    <div class="item"><div class="item-name"><span>Seasonal Rotating<span class="sub">(Butternut Squash Soup)</span></span><svg class="tag" style="margin-left:26px;align-self:flex-start;margin-top:2px"><use href="#icon-gf"/></svg><svg class="tag" style="align-self:flex-start;margin-top:2px"><use href="#icon-vegan"/></svg></div>Butternut squash blended with warm spices,<br>and coconut milk.</div>
  </section>

  <section class="section-body" style="left:855px;top:703px">
    <div class="item"><div class="item-name">Soup + Salad</div>“Your choice of soup and side salad.<br>16oz soup + 38oz salad”</div>
    <div class="item"><div class="item-name">Avo Toast Combo</div>Half avocado toast and your choice of soup. 16oz</div>
    <div class="item"><div class="item-name">Soup + Sammy</div>“Your choice of soup and sandwich.<br>16oz soup + Sandwich”</div>
  </section>

  <div class="legend" aria-label="Dietary key">
    <span><svg class="tag"><use href="#icon-vegan"/></svg>Vegan</span>
    <span><svg class="tag"><use href="#icon-vegetarian"/></svg>Vegetarian</span>
    <span><svg class="tag"><use href="#icon-nuts"/></svg>Contains Nuts</span>
    <span><svg class="tag"><use href="#icon-gf"/></svg>Gluten Free</span>
  </div>
</main>
</body>
</html>
```